Harborline Crest Insurance Services

we are a high end insurance agency we specialize on Auto | Home | Business | Life looking for something professional and luxuries at the same time. if you guys need anything else please let me know.

Auto | Home | Business | Life must be under logo on the back with black background.

i want the back part to be black with our gold logo on it.

Target Market(s)

Auto | Home | Business | Life

Industry/Entity Type

Insurance Broker

Contact Information for Business Card

My logo is gold so a black in the back would be nice.

Font styles to use
Serif

Colors
000000

Requirements
Must have
• Big logo on the back with black background.

```html
<!DOCTYPE html>
<html lang="en">
<head>
<meta charset="utf-8">
<title>Harborline Crest Insurance Services – Business Card</title>
<link href="https://fonts.googleapis.com/css2?family=Cinzel:wght@700&family=Arimo:wght@400;700&display=swap" rel="stylesheet">
<style>
  :root {
    --page: #2b2623;
    --card: #0e0e0e;
    --card-edge: #1a1a1a;
    --gold: #e0ad2c;
    --gold-soft: #c9992a;
    --silver: #9a9a9a;
    --text: #f2f2f2;
    --muted: #8a8a8a;
    --rule: #5a5a5a;
  }
  * { box-sizing: border-box; margin: 0; padding: 0; }
  html, body { width: 1200px; height: 864px; overflow: hidden; }
  body {
    background: var(--page);
    font-family: "Arimo", Arial, sans-serif;
    display: flex;
    align-items: center;
    justify-content: center;
    gap: 40px;
  }
  .card {
    width: 540px;
    height: 308px;
    background: var(--card);
    border: 1px solid var(--card-edge);
    border-radius: 3px;
    position: relative;
    box-shadow: 0 14px 30px rgba(0,0,0,0.45);
  }

  /* Back side */
  .card-back {
    display: flex;
    flex-direction: column;
    justify-content: center;
    padding: 0 44px;
  }
  .brand-row { display: flex; align-items: center; gap: 16px; }
  .brand-dot {
    width: 40px; height: 40px; border-radius: 50%;
    background: var(--gold); flex: none;
  }
  .brand-name {
    font-family: "Cinzel", Georgia, serif;
    font-weight: 700;
    color: var(--gold);
    font-size: 25px;
    line-height: 1.15;
    letter-spacing: 0.5px;
  }
  .services {
    margin-top: 12px;
    margin-left: 56px;
    color: var(--silver);
    font-size: 11px;
    letter-spacing: 1.5px;
  }
  .website-back {
    margin-top: 40px;
    margin-left: 4px;
    color: var(--muted);
    font-size: 12px;
    letter-spacing: 3px;
  }

  /* Front side */
  .card-front { display: flex; align-items: center; }
  .emblem-area {
    width: 258px;
    height: 100%;
    display: flex;
    flex-direction: column;
    align-items: center;
    justify-content: center;
    gap: 14px;
    padding: 0 28px;
  }
  .emblem-dot { width: 46px; height: 46px; border-radius: 50%; background: var(--gold); }
  .emblem-name {
    font-family: "Cinzel", Georgia, serif;
    font-weight: 700;
    color: var(--gold);
    font-size: 22px;
    text-align: center;
    line-height: 1.2;
  }
  .divider {
    width: 1px;
    height: 210px;
    background: linear-gradient(to bottom, transparent, var(--rule), transparent);
  }
  .contact { padding-left: 22px; color: var(--text); }
  .person-name { color: var(--gold); font-size: 17px; font-weight: 700; }
  .person-role { font-size: 15px; margin-bottom: 10px; }
  .address { font-size: 13px; line-height: 1.45; margin-bottom: 8px; }
  .contact-list { list-style: none; font-size: 13.5px; }
  .contact-list li { display: flex; align-items: center; gap: 10px; line-height: 21px; }
  .contact-list svg { width: 13px; height: 13px; fill: var(--gold); flex: none; }
</style>
</head>
<body>

  <section class="card card-back">
    <div class="brand-row">
      <span class="brand-dot"></span>
      <div class="brand-name">Harborline Crest<br>Insurance Services</div>
    </div>
    <p class="services">AUTO | HOME | BUSINESS | LIFE</p>
    <p class="website-back">www.harborlinecrest.com</p>
  </section>

  <section class="card card-front">
    <div class="emblem-area">
      <span class="emblem-dot"></span>
      <div class="emblem-name">Harborline Crest</div>
    </div>
    <div class="divider"></div>
    <div class="contact">
      <p class="person-name">Marcus Hale</p>
      <p class="person-role">President</p>
      <p class="address">4170 Linden Crest Road<br>Bayview Park, NY 11920</p>
      <ul class="contact-list">
        <li><svg viewBox="0 0 16 16"><path d="M3 1h3l1.5 4-2 1.2a9 9 0 0 0 4.3 4.3L11 8.5l4 1.5v3a2 2 0 0 1-2 2A12 12 0 0 1 1 3a2 2 0 0 1 2-2z"/></svg>555 0142 7788</li>
        <li><svg viewBox="0 0 16 16"><path d="M4 0h8a1 1 0 0 1 1 1v14a1 1 0 0 1-1 1H4a1 1 0 0 1-1-1V1a1 1 0 0 1 1-1zm1 2v10h6V2zm3 11a1 1 0 1 0 0 2 1 1 0 0 0 0-2z"/></svg>555 0193 4621</li>
        <li><svg viewBox="0 0 16 16"><path d="M4 0h7v5H4zM1 6h14v8H1zm3 2v2h8V8z"/></svg>555 0167 3309</li>
        <li><svg viewBox="0 0 16 16"><path d="M0 3h16v10H0zm1.5 1.5v.3L8 9l6.5-4.2v-.3z"/></svg>marcus@harborlinecrest.com</li>
        <li><svg viewBox="0 0 16 16"><path d="M8 0a8 8 0 1 0 0 16A8 8 0 0 0 8 0zm0 2a6 6 0 0 1 5.6 4H2.4A6 6 0 0 1 8 2zM2.2 8h11.6a6 6 0 0 1-11.6 0z"/></svg>www.harborlinecrest.com</li>
      </ul>
    </div>
  </section>

</body>
</html>
```